Verostel business card

Business card for sustainable investment company called "Verostel". Verostel is an exchange platform selling carbon credits between buyers and sellers. Carbon Credits are an environmental commodity for reducing global carbon emissions.

the card should obviously have our logo and the theme should be sustainability/environment mixed with a trading platform.

Contact Information for Business Card

Logo, Name, Title, Phone, Email

Colors
0054AA
0677BA
7BADD7
CADEEF
E8F1F8
0094D4
00A9DD
6FCCEA
C7EBF8
E9F6FB
00AB8E
00BBA5
67D7C9
C6EFE9
E9F9F6
59FF00
82FF00
B8FF75
E3FFCB
F4FFEA

```html
<!DOCTYPE html>
<html lang="en">
<head>
<meta charset="utf-8">
<title>Verostel business card</title>
<link rel="stylesheet" href="https://fonts.googleapis.com/css2?family=Montserrat:wght@700&family=Open+Sans:wght@400;600;700&display=swap">
<style>
  :root {
    --stage: #1e1f23;
    --navy: #142b53;
    --edge: #62c6d8;
    --accent: #5b9fd4;
    --accent-soft: #6cc3da;
    --white: #ffffff;
    --rule: #c9d6e6;
  }
  * { margin: 0; padding: 0; box-sizing: border-box; }
  html, body {
    width: 1200px; height: 780px; overflow: hidden;
    background: var(--stage);
  }
  .canvas {
    position: relative; width: 1200px; height: 780px;
    display: flex; align-items: center; justify-content: center; gap: 40px;
  }
  .card {
    position: relative; width: 540px; height: 308px;
    background: var(--navy);
    border-left: 7px solid var(--edge);
    overflow: hidden;
  }
  .front {
    display: flex; align-items: center; justify-content: center; gap: 18px;
  }
  .brand-dot {
    width: 34px; height: 34px; border-radius: 50%;
    background: var(--accent);
  }
  .wordmark {
    font-family: "Montserrat", sans-serif; font-weight: 700;
    font-size: 44px; letter-spacing: 1px; color: var(--white);
    text-transform: uppercase;
  }
  .back { display: flex; }
  .back-brand {
    width: 255px; display: flex; flex-direction: column;
    align-items: center; justify-content: center; gap: 14px;
  }
  .back-brand .brand-dot { width: 70px; height: 70px; }
  .back-brand .wordmark-large {
    font-family: "Montserrat", sans-serif; font-weight: 700;
    font-size: 30px; color: var(--accent); text-transform: uppercase;
  }
  .divider {
    width: 1px; margin: 48px 0 46px; background: var(--rule); opacity: .8;
  }
  .details {
    flex: 1; padding: 52px 20px 0 26px;
    font-family: "Open Sans", sans-serif; color: var(--white);
  }
  .person-name {
    font-weight: 700; font-size: 25px; color: var(--accent-soft); line-height: 1.1;
  }
  .person-title { font-weight: 600; font-size: 14px; margin-top: 3px; }
  .address { font-size: 13px; line-height: 1.45; margin-top: 20px; }
  .contact { list-style: none; margin-top: 14px; font-size: 13px; line-height: 1.6; }
  .contact li { display: flex; align-items: center; gap: 9px; }
  .contact svg { width: 13px; height: 13px; fill: var(--accent); flex: none; }
</style>
</head>
<body>
<main class="canvas">
  <section class="card front" aria-label="Card front">
    <span class="brand-dot" aria-hidden="true"></span>
    <span class="wordmark">Verostel</span>
  </section>

  <section class="card back" aria-label="Card back">
    <div class="back-brand">
      <span class="brand-dot" aria-hidden="true"></span>
      <span class="wordmark-large">Verostel</span>
    </div>
    <div class="divider" aria-hidden="true"></div>
    <div class="details">
      <p class="person-name">Marta Velisek</p>
      <p class="person-title">Managing Director</p>
      <p class="address">418 Linden Ridge Rd. Suite 300<br>Harlow, TX 75990</p>
      <ul class="contact">
        <li>
          <svg viewBox="0 0 24 24" aria-hidden="true"><path d="M6.6 10.8a15.2 15.2 0 0 0 6.6 6.6l2.2-2.2a1 1 0 0 1 1-.25 11.4 11.4 0 0 0 3.6.57 1 1 0 0 1 1 1V20a1 1 0 0 1-1 1A17 17 0 0 1 3 4a1 1 0 0 1 1-1h3.5a1 1 0 0 1 1 1c0 1.25.2 2.45.57 3.57a1 1 0 0 1-.25 1z"/></svg>
          (555) 214-6083
        </li>
        <li>
          <svg viewBox="0 0 24 24" aria-hidden="true"><path d="M2 5h20v14H2zm2 2v.5l8 5 8-5V7zm0 2.9V17h16V9.9l-8 5z"/></svg>
          info@verostel.com
        </li>
        <li>
          <svg viewBox="0 0 24 24" aria-hidden="true"><path d="M12 2a10 10 0 1 0 0 20 10 10 0 0 0 0-20zm6.9 6h-3a15 15 0 0 0-1.3-3.9A8 8 0 0 1 18.9 8zM12 4c.9 1.2 1.6 2.5 2 4h-4c.4-1.5 1.1-2.8 2-4zM4.3 14a8 8 0 0 1 0-4h3.4a16 16 0 0 0 0 4zm.8 2h3a15 15 0 0 0 1.3 3.9A8 8 0 0 1 5.1 16zM8 8H5.1a8 8 0 0 1 4.3-3.9A15 15 0 0 0 8.1 8zm4 12c-.9-1.2-1.6-2.5-2-4h4c-.4 1.5-1.1 2.8-2 4zm2.3-6H9.7a14 14 0 0 1 0-4h4.6a14 14 0 0 1 0 4zm.3 5.9a15 15 0 0 0 1.3-3.9h3a8 8 0 0 1-4.3 3.9zM16.3 14a16 16 0 0 0 0-4h3.4a8 8 0 0 1 0 4z"/></svg>
          www.verostel.com
        </li>
      </ul>
    </div>
  </section>
</main>
</body>
</html>
```